Business Card Design Project

I have attached the logo and the colour pallete for the branding for the company.

Creative designs for business cards are needed.

The Company is modern corporate.

Industry/Entity Type

Business

```html
<!DOCTYPE html>
<html lang="en">
<head>
<meta charset="utf-8">
<title>Pathwise Business Cards</title>
<link rel="stylesheet" href="https://fonts.googleapis.com/css2?family=Open+Sans:wght@400;700&display=swap">
<style>
  :root {
    --backdrop: #8a5d3b;
    --card-light: #f29a52;
    --card-mid: #ec8a3e;
    --card-dark: #e07a2e;
    --ink-white: #ffffff;
    --card-shadow: rgba(40, 20, 5, 0.45);
  }
  * { margin: 0; padding: 0; box-sizing: border-box; }
  html, body {
    width: 1200px;
    height: 767px;
    overflow: hidden;
  }
  body {
    background: var(--backdrop);
    font-family: "Open Sans", Arial, sans-serif;
    color: var(--ink-white);
  }
  .canvas {
    position: relative;
    width: 1200px;
    height: 767px;
  }
  .card {
    position: absolute;
    width: 520px;
    height: 300px;
    background: linear-gradient(160deg, var(--card-light) 0%, var(--card-mid) 55%, var(--card-dark) 100%);
    box-shadow: 6px 10px 22px var(--card-shadow);
  }
  .card-front {
    left: 170px;
    top: 70px;
    display: flex;
    align-items: center;
    justify-content: center;
  }
  .brand-name {
    font-weight: 400;
    color: var(--ink-white);
    letter-spacing: 0.5px;
  }
  .card-front .brand-name {
    font-size: 64px;
  }
  .card-back {
    left: 520px;
    top: 400px;
  }
  .card-back .brand-name {
    position: absolute;
    top: 26px;
    right: 30px;
    font-size: 32px;
  }
  .company-name {
    position: absolute;
    left: 70px;
    top: 96px;
    font-size: 21px;
    font-weight: 700;
  }
  .contact-list {
    position: absolute;
    left: 70px;
    top: 150px;
    list-style: none;
    font-size: 16px;
    line-height: 23px;
  }
</style>
</head>
<body>
  <main class="canvas">
    <section class="card card-front" aria-label="Business card front">
      <span class="brand-name">pathwise</span>
    </section>
    <section class="card card-back" aria-label="Business card back">
      <span class="brand-name">pathwise</span>
      <h2 class="company-name">Company Name</h2>
      <ul class="contact-list">
        <li>Phone: xxxxxxxxxx</li>
        <li>Mobile: xxxxxxxxxx</li>
        <li>Email: xxxxxxxxxx</li>
        <li>Web: xxxxxxxxxxx</li>
      </ul>
    </section>
  </main>
</body>
</html>
```